Mail order Nursery needs banner for promoting perennials that compliment roses.

banner should be 1135 wide x165 tall. We have an existing one displayed but we are not happy with the way it is washed out. Use your creativity to give us something that pops. Would love to see some watercolor or some other form of image other than just words washed across a stock photo. Banner needs to read Perennial Companions for Roses or some variation of that. Colors need to compliment our current theme. You can view the page and banner I want to replace at www.meadowlarkbloomyard.com. The banner we want to replace has been uploaded to the pixel forum file drop box. Thanks for your help and I look forward to seeing what you guys come up with. EDIT: I don't think I was clear enough in by brief. This banner promotes the sale of plants that look good planted with roses. We are getting to many submissions that are using only roses as the backdrop. We are looking for different types of plants that you would grow in your garden to compliment your roses. Thanks for all your hard work.

Target Market(s)

Home owners between 30 and 65

Industry/Entity Type

Nursery

Colors
33a6d7
e667a6

Requirements
Must have
• Text promotion perennials that compliment roses.... does not have to be those exact words but get the point across
Should not have
• Stock Photos with simple text washed across it.

```html
<!DOCTYPE html>
<html lang="en">
<head>
<meta charset="utf-8">
<title>Perennial Companions for Roses</title>
<link rel="stylesheet" href="https://fonts.googleapis.com/css2?family=Cinzel:wght@400&family=Parisienne&display=swap">
<style>
  :root {
    --bloom-blue: #33a6d7;
    --title-blue: #5cbbe4;
    --sky-wash: #8fd0f0;
    --deep-blue: #1a78d6;
    --lavender: #a9a6e6;
    --rose-pink: #e667a6;
    --script-pink: #e874b2;
    --soft-pink: #f3a6d2;
    --hot-pink: #f0287a;
    --paper: #ffffff;
  }
  html, body {
    margin: 0;
    padding: 0;
    overflow: hidden;
    background: var(--paper);
  }
  .banner {
    position: relative;
    width: 1200px;
    height: 174px;
    overflow: hidden;
    background: var(--paper);
  }
  .wash-band {
    position: absolute;
    left: 0;
    top: 0;
    width: 1200px;
    height: 174px;
  }
  .blue-florals {
    position: absolute;
    left: 0;
    top: 0;
    width: 320px;
    height: 174px;
    background: linear-gradient(160deg,
      var(--sky-wash) 0%,
      var(--bloom-blue) 30%,
      var(--deep-blue) 55%,
      var(--bloom-blue) 78%,
      var(--sky-wash) 100%);
    -webkit-mask-image: linear-gradient(90deg, #000 0%, #000 72%, transparent 100%);
    mask-image: linear-gradient(90deg, #000 0%, #000 72%, transparent 100%);
  }
  .pink-bloom {
    position: absolute;
    right: 0;
    top: 0;
    width: 300px;
    height: 174px;
    background: linear-gradient(200deg,
      var(--soft-pink) 0%,
      var(--rose-pink) 35%,
      var(--hot-pink) 60%,
      var(--rose-pink) 80%,
      var(--soft-pink) 100%);
    -webkit-mask-image: linear-gradient(270deg, #000 0%, #000 70%, transparent 100%);
    mask-image: linear-gradient(270deg, #000 0%, #000 70%, transparent 100%);
  }
  .title {
    position: absolute;
    left: 0;
    top: 0;
    width: 1200px;
    height: 174px;
    margin: 0;
    font-weight: 400;
  }
  .title-main {
    position: absolute;
    left: 332px;
    top: 24px;
    width: 516px;
    text-align: center;
    font-family: "Cinzel", "Times New Roman", serif;
    font-size: 41px;
    line-height: 48px;
    letter-spacing: 0.3px;
    color: var(--title-blue);
    white-space: nowrap;
  }
  .title-sub {
    position: absolute;
    left: 332px;
    top: 68px;
    width: 516px;
    height: 54px;
    display: flex;
    align-items: center;
    gap: 10px;
  }
  .rule {
    flex: 1;
    height: 1.5px;
    margin-top: 4px;
    background: var(--rose-pink);
  }
  .script {
    font-family: "Parisienne", cursive;
    font-size: 52px;
    line-height: 54px;
    color: var(--script-pink);
    white-space: nowrap;
  }
</style>
</head>
<body>
  <div class="banner">
    <svg class="wash-band" viewBox="0 0 1200 174" role="img" aria-label="Blue and lavender watercolour wash along the lower edge">
      <defs>
        <linearGradient id="wash-tones" x1="0" y1="0" x2="1" y2="0">
          <stop offset="0" stop-color="#8fd0f0"/>
          <stop offset="0.2" stop-color="#33a6d7"/>
          <stop offset="0.45" stop-color="#a9a6e6"/>
          <stop offset="0.65" stop-color="#33a6d7"/>
          <stop offset="0.85" stop-color="#8fd0f0"/>
          <stop offset="1" stop-color="#a9a6e6"/>
        </linearGradient>
      </defs>
      <path fill="url(#wash-tones)" opacity="0.9"
        d="M270 174 C300 160 340 150 380 140 C420 134 470 146 510 142 C560 138 600 150 650 146 C700 142 740 152 790 148 C840 144 880 150 930 146 C980 142 1040 150 1100 144 L1200 140 L1200 174 Z"/>
    </svg>
    <div class="blue-florals" role="img" aria-label="Blue watercolour painting of garden perennials"></div>
    <div class="pink-bloom" role="img" aria-label="Pink watercolour painting of a large open flower"></div>
    <h1 class="title">
      <span class="title-main">Perennial Companions</span>
      <span class="title-sub">
        <span class="rule"></span>
        <span class="script">for Roses</span>
        <span class="rule"></span>
      </span>
    </h1>
  </div>
</body>
</html>
```